Criação de Papelaria Profissional para Contabilidade & Finanças
" ESTOU INICANDO AGORA O ESCRITORIO DE CONTABILIDADE, QUERO ATUAR NO RAMO DE TREINAMENTO ATRAVÉS DO COACHING , FAZER CONSULTORIAS NA AREA CONTABIL, SERVIÇOS CONTABEIS EM GERAL, DESDE O MICROEMPREENDEDOR ATÉ O A EMPRESA DE GRANDE PORTE LUCRO REAL "

```html
<!DOCTYPE html>
<html lang="pt-BR">
<head>
<meta charset="utf-8">
<title>TVL Consultoria Contábil &amp; Fiscal — Envelope</title>
<link rel="stylesheet" href="https://fonts.googleapis.com/css2?family=Montserrat:wght@400;600;700&display=swap">
<style>
  :root{
    --stage:#2b2d31;
    --paper:#ffffff;
    --navy:#0b1638;
    --navy-deep:#050b22;
    --navy-mid:#13245a;
    --gold:#c9a24a;
    --ink:#3a3f4b;
    --ghost:#e9ecf1;
  }
  *{box-sizing:border-box;margin:0;padding:0}
  html,body{width:1200px;height:1200px;overflow:hidden;background:var(--stage)}
  body{font-family:"Montserrat",sans-serif;position:relative}
  .envelope{position:absolute;top:310px;width:430px;height:580px;overflow:hidden;box-shadow:0 10px 30px rgba(0,0,0,.45)}
  .envelope--front{left:150px;background:var(--paper)}
  .envelope--back{left:620px;background:radial-gradient(ellipse at 60% 45%,var(--navy-mid) 0%,var(--navy) 45%,var(--navy-deep) 100%)}
  .flap{position:absolute;top:0;left:0;width:430px;height:80px}
  .front-decor{position:absolute;left:30px;top:190px;width:380px;height:200px;border-radius:50% 50% 10% 10%;
    background:radial-gradient(ellipse at 60% 40%,var(--ghost) 0%,rgba(233,236,241,.5) 55%,rgba(255,255,255,0) 80%)}
  .brand{display:flex;align-items:center;gap:6px;color:var(--gold);font-weight:700;letter-spacing:.02em}
  .brand__mark{background:var(--gold)}
  .front-brand{position:absolute;left:122px;top:462px}
  .front-brand .brand{font-size:22px;color:var(--navy)}
  .front-brand .brand__mark{width:12px;height:22px;background:var(--navy)}
  .front-brand .tagline{font-size:5px;color:var(--ink);margin-top:2px;letter-spacing:.05em}
  .contacts{position:absolute;left:18px;right:18px;top:520px;display:flex;justify-content:space-between;font-size:6px;color:var(--ink);line-height:1.7}
  .contact{display:flex;align-items:flex-start;gap:4px}
  .contact svg{flex:none;margin-top:2px}
  .gold-rule{position:absolute;height:1px;background:var(--gold)}
  .front-rule{left:0;right:0;top:555px}
  .front-band{position:absolute;left:0;right:0;top:557px;bottom:0;background:var(--navy)}
  .back-decor{position:absolute;left:0;top:0;width:200px;height:520px;
    background:linear-gradient(90deg,rgba(30,50,110,.55) 0%,rgba(20,36,90,.25) 60%,rgba(11,22,56,0) 100%)}
  .back-brand{position:absolute;left:0;right:0;top:238px;display:flex;flex-direction:column;align-items:center}
  .back-brand .brand{font-size:48px}
  .back-brand .brand__mark{width:22px;height:46px}
  .back-brand .tagline{font-size:9px;color:var(--gold);font-weight:700;letter-spacing:.04em;margin:2px 0 0 30px}
  .back-rule{left:22px;right:22px;top:540px;opacity:.85}
</style>
</head>
<body>
  <section class="envelope envelope--front" aria-label="Frente do envelope">
    <svg class="flap" viewBox="0 0 430 80" aria-hidden="true">
      <path d="M0 0H430V36H396Q388 36 386 44L384 58Q382 70 370 70H60Q48 70 46 58L44 44Q42 36 34 36H0Z" fill="#0b1638"/>
    </svg>
    <div class="front-decor" role="img" aria-label="Símbolo da marca em marca d'água suave"></div>
    <div class="front-brand">
      <div class="brand"><span class="brand__mark"></span>TVL</div>
      <div class="tagline">CONSULTORIA CONTÁBIL &amp; FISCAL</div>
    </div>
    <div class="contacts">
      <div class="contact">
        <svg width="7" height="7" viewBox="0 0 10 10"><circle cx="5" cy="5" r="4.5" fill="none" stroke="#3a3f4b"/><path d="M3.5 3l1 1-.5.7 1.3 1.3.7-.5 1 1-.8.8C4.6 7 3 5.4 2.7 3.8z" fill="#3a3f4b"/></svg>
        <div>+55 11 3000-0000<br>+55 11 90000-0000</div>
      </div>
      <div class="contact">
        <svg width="7" height="7" viewBox="0 0 10 10"><circle cx="5" cy="5" r="4.5" fill="none" stroke="#3a3f4b"/><path d="M5 2.5a1.7 1.7 0 0 1 1.7 1.7C6.7 5.5 5 7.5 5 7.5S3.3 5.5 3.3 4.2A1.7 1.7 0 0 1 5 2.5z" fill="#3a3f4b"/></svg>
        <div>Rua das Acácias, 120, sala 4<br>Centro, São Paulo/SP · CEP 01000-000</div>
      </div>
      <div class="contact">
        <svg width="7" height="7" viewBox="0 0 10 10"><circle cx="5" cy="5" r="4.5" fill="none" stroke="#3a3f4b"/><rect x="2.8" y="3.4" width="4.4" height="3.2" fill="none" stroke="#3a3f4b" stroke-width=".7"/><path d="M2.8 3.4L5 5.2 7.2 3.4" fill="none" stroke="#3a3f4b" stroke-width=".7"/></svg>
        <div>contato@tvlcontabil.com.br<br>www.tvlcontabil.com.br</div>
      </div>
    </div>
    <div class="gold-rule front-rule"></div>
    <div class="front-band"></div>
  </section>

  <section class="envelope envelope--back" aria-label="Verso do envelope">
    <div class="back-decor" role="img" aria-label="Padrão decorativo de divisas em azul sobre o fundo"></div>
    <div class="back-brand">
      <div class="brand"><span class="brand__mark"></span>TVL</div>
      <div class="tagline">CONSULTORIA CONTÁBIL &amp; FISCAL</div>
    </div>
    <div class="gold-rule back-rule"></div>
  </section>
</body>
</html>
```